Bildmark Speech for a trade show in Las Vegas

I've tried to create the powerpoint on my own. I used a template, but am not satisfied with the look and feel. I'd like something more professional looking. I need this powerpoint for an upcoming speech. I need the ppt to be in a format in which I can edit it for last-minute changes before my speech.

The Power Point has a lot of slides, but mostly I'm looking for a few good backgrounds so that every slide doesn't have to be completely unique. Plus, if you can clean up some of my graphics, that would be great too. Feel free to message me with any questions. Happy to help out.

Target Market(s)

Leaders in Construction and Manufacturing

Industry/Entity Type

Construction

Font styles to use
Sans Serif

Colors

Designer to choose colors to be used in the design.

Requirements
Must have
• The ability for me to edit the slides so that I can do some last-minute changes.
• I need to have the Bildmark/TerraMix logo (small round logo) on the bottom of each slide (or at least most of them).
Nice to have
• Pictures of people on construction sites using heavy equipment. (Backhoes, Loaders, Gravlers, Trench Falcon products, Ironmoth products, Harlan Voss products, etc)

```html
<!DOCTYPE html>
<html lang="en">
<head>
<meta charset="utf-8">
<title>Bildmark/TerraMix Speech Deck</title>
<link href="https://fonts.googleapis.com/css2?family=Archivo:wght@400;600;700;800;900&family=Archivo+Black&family=Arimo:wght@400;700&display=swap" rel="stylesheet">
<style>
:root{
  --canvas:#c3c4c6;
  --navy:#1b3f8e;
  --navy-dark:#122b66;
  --page-box:#5270d2;
  --red:#b4252f;
  --red-bright:#e8382a;
  --blue:#1f3f9a;
  --teal:#5acfb0;
  --teal-dark:#2eaa87;
  --orange:#fb7d1e;
  --orange-dark:#e0600d;
  --green:#82d21e;
  --ink:#222;
  --mint:#c6ece1;
}
*{margin:0;padding:0;box-sizing:border-box}
html,body{width:1200px;height:909px;overflow:hidden;background:var(--canvas)}
.stage{position:absolute;left:0;top:0;width:2212px;height:1676px;transform:scale(.5425);transform-origin:0 0;font-family:"Arimo",Arial,sans-serif;color:var(--ink)}
.slide{position:absolute;width:715px;height:403px;background:#fff;overflow:hidden}
.abs{position:absolute}
.title{position:absolute;left:0;right:0;top:22px;text-align:center;font-family:"Archivo",Arial,sans-serif;font-weight:800;font-size:19px;letter-spacing:1px;color:#333}
.footer{position:absolute;left:0;bottom:0;width:100%;height:22px;background:var(--navy);color:#fff;font-size:9px}
.footer .brand{position:absolute;left:55px;top:6px}
.footer .date{position:absolute;left:221px;top:6px}
.footer .page{position:absolute;left:635px;top:0;width:32px;height:22px;background:var(--page-box);text-align:center;line-height:22px}
.footer .seal{position:absolute;left:337px;top:-20px;width:42px;height:42px;border-radius:50%;background:#fff;border:3px solid var(--navy);display:flex;align-items:center;justify-content:center;font-size:6px;font-weight:700;color:var(--navy);text-align:center;line-height:1.1}
.center{text-align:center}
/* slide 1 */
.brandmark{position:absolute;left:0;right:0;top:70px;text-align:center;font-family:"Archivo",sans-serif;font-weight:800;font-size:22px;color:var(--navy)}
.brandmark .dot{display:block;margin:0 auto 12px;width:80px;height:80px;border-radius:50%;background:var(--orange)}
.welcome{position:absolute;left:0;right:0;top:198px;text-align:center;font-family:"Archivo Black",sans-serif;font-size:50px;letter-spacing:2px;color:var(--red)}
.subtitle{position:absolute;left:0;right:0;top:264px;text-align:center;font-size:18px;color:var(--blue)}
.pill{position:absolute;left:270px;top:295px;width:176px;height:38px;border-radius:19px;background:var(--navy);border:3px solid #f4b320;color:#fff;font-size:13px;text-align:center;line-height:32px}
.pill b{font-weight:700}
/* slide 2 */
.quote-badge{position:absolute;left:331px;top:88px;width:52px;height:52px;border-radius:50%;background:var(--teal);color:#fff;font-family:"Archivo Black",sans-serif;font-size:34px;text-align:center;line-height:62px}
.question{position:absolute;left:0;right:0;top:182px;text-align:center;font-size:22px;line-height:29px;color:#222}
.stop{color:var(--red-bright);font-weight:700}
.start{color:var(--blue);font-weight:700}
/* slide 4 */
.side-note{position:absolute;font-size:12px;line-height:16px;color:#444}
/* slide 5 */
.panel{position:absolute;left:0;top:91px;width:715px;height:220px;background:#f5f7fa;border-top:1px solid #555;border-bottom:1px solid #555}
.disc{position:absolute;width:360px;text-align:center;font-size:12px;color:#222}
/* slide 6 */
.photo{position:absolute;left:0;top:0;width:330px;height:381px;background:linear-gradient(90deg,#9a8e88 0%,#c9c2bf 55%,#eeeceb 85%,rgba(255,255,255,0) 100%)}
.disc-head{position:absolute;right:28px;top:26px;font-family:"Archivo",sans-serif;font-weight:800;font-size:17px}
.disc-body{position:absolute;right:28px;top:72px;width:290px;text-align:right;font-size:22px;line-height:29px;color:#333}
/* slide 7 */
.comm-grid{position:absolute;left:48px;top:79px;width:403px;height:255px;border-collapse:collapse}
.comm-grid td{border:1px solid #ccc;width:134px;height:127px;text-align:center;vertical-align:bottom;font-size:10px;font-weight:700;position:relative}
.comm-grid td span{display:block;border-top:1px solid #ccc;background:#f6f6f6;padding:4px 0}
.comm-grid td svg{position:absolute;left:50%;top:38px;transform:translateX(-50%)}
/* slide 8 */
.stat{position:absolute;top:137px;width:224px;height:143px;color:#fff;text-align:center}
.stat .num{height:102px;line-height:102px;font-family:"Archivo Black",sans-serif;font-size:40px}
.stat .num sup{font-family:"Arimo",sans-serif;font-size:22px;vertical-align:18px}
.stat .lbl{height:41px;line-height:41px;font-family:"Archivo",sans-serif;font-weight:700;font-size:12px;letter-spacing:3px}
/* slide 9 */
.quad{position:absolute;width:213px;height:80px;color:#fff;text-align:center;border-radius:3px}
.quad b{display:block;margin-top:22px;font-family:"Archivo",sans-serif;font-weight:800;font-size:13px;letter-spacing:3px}
.quad i{font-style:normal;font-size:9px}
.axis-lbl{position:absolute;font-size:13px;color:#f39a3a;white-space:nowrap}
/* slide 10 */
.eng-head{position:absolute;left:0;right:0;top:14px;text-align:center;font-family:"Archivo",sans-serif;font-weight:800;font-size:11.5px}
.figure{position:absolute;background:linear-gradient(180deg,#2a2e3a,#444 60%,#1a1a1a)}
.eng-table{position:absolute;left:168px;top:83px;width:389px;border-collapse:collapse;font-size:7.4px}
.eng-table td{height:22.6px;border-bottom:1px solid #e6e6e6;text-align:center}
.eng-table tr:nth-child(odd){background:#f3f3f3}
.eng-table .hi{color:var(--teal-dark);font-size:10px;width:66px}
.eng-table .lo{color:var(--orange-dark);font-size:10px;width:60px}
.eng-table tr.flag td{background:#fdf3e4;border-top:1px solid #f4b84a;border-bottom:1px solid #f4b84a}
.vert{position:absolute;transform:rotate(-90deg);transform-origin:0 0;font-size:13px;letter-spacing:.5px;white-space:nowrap}
/* slide 11 */
.fat-head{position:absolute;left:55px;top:24px;font-weight:700;font-size:12.5px;line-height:16px}
.fat-list{position:absolute;top:92px;list-style:none;font-size:11.5px}
.fat-list li{height:18.8px}
.fat-list li::before{content:"";display:inline-block;border-left:6px solid var(--orange);border-top:3.5px solid transparent;border-bottom:3.5px solid transparent;margin-right:11px}
/* slide 12 */
.thanks{position:absolute;left:0;right:0;top:176px;text-align:center;font-family:"Archivo Black",sans-serif;font-size:48px;color:var(--navy-dark)}
.contact{position:absolute;top:340px;width:179px;height:63px;color:#111;text-align:center;font-size:10px;font-weight:700}
.contact svg{display:block;margin:9px auto 12px}
</style>
</head>
<body>
<div class="stage">

<!-- 1 welcome -->
<section class="slide" style="left:22px;top:16px">
  <div class="brandmark"><span class="dot"></span>BILDMARK/TERRAMIX</div>
  <div class="welcome">WELCOME</div>
  <div class="subtitle">Place your subtitle here</div>
  <div class="pill">Presented by <b>Dana Reyes</b></div>
</section>

<!-- 2 start & stop -->
<section class="slide" style="left:748px;top:16px">
  <div class="title">STARTING &amp; STOPPING</div>
  <div class="quote-badge">”</div>
  <div class="question">In light of what you’ve just heard, what<br>are some things you need to either<br><span class="stop">STOP</span> or <span class="start">START</span> doing?</div>
  <footer class="footer"><span class="brand">BILDMARK / TERRAMIX</span><span class="date">2/7/2020</span><span class="seal">BILDMARK</span><span class="page">2</span></footer>
</section>

<!-- 3 lift effect -->
<section class="slide" style="left:1475px;top:16px">
  <div class="title" style="top:22px">LEADERS WORTH FOLLOWING</div>
  <div class="abs center" style="left:0;right:0;top:48px;font-size:13px;letter-spacing:2px;color:var(--blue)">The Lift Effect</div>
  <svg class="abs" style="left:0;top:0" width="715" height="380" viewBox="0 0 715 380">
    <polygon points="179,216 342,216 179,345" fill="#4a6ea8"/>
    <g stroke="#fff" stroke-width="1.5" fill="#fff">
      <line x1="200" y1="330" x2="200" y2="222"/><polygon points="196,224 200,216 204,224"/>
      <line x1="220" y1="314" x2="220" y2="222"/><polygon points="216,224 220,216 224,224"/>
      <line x1="241" y1="298" x2="241" y2="222"/><polygon points="237,224 241,216 245,224"/>
      <line x1="262" y1="281" x2="262" y2="222"/><polygon points="258,224 262,216 266,224"/>
      <line x1="283" y1="265" x2="283" y2="222"/><polygon points="279,224 283,216 287,224"/>
      <line x1="304" y1="248" x2="304" y2="222"/><polygon points="300,224 304,216 308,224"/>
    </g>
    <line x1="179" y1="216" x2="537" y2="216" stroke="#f3b63a" stroke-width="2"/>
    <line x1="179" y1="345" x2="495" y2="96" stroke="#7fd33a" stroke-width="2"/>
    <polygon points="502,91 489,94 496,102" fill="#7fd33a"/>
    <line x1="179" y1="345" x2="179" y2="92" stroke="#111" stroke-width="1.5"/>
    <polygon points="175,94 179,86 183,94" fill="#111"/>
    <line x1="179" y1="345" x2="532" y2="345" stroke="#111" stroke-width="1.5"/>
    <polygon points="530,341 538,345 530,349" fill="#111"/>
    <text x="355" y="200" transform="rotate(-38 355 200)" font-size="13" fill="#c2272d" font-family="Arimo,sans-serif">Size of your organization</text>
    <text x="387" y="232" font-size="12" fill="#1f3f9a" font-family="Arimo,sans-serif">Your Leadership Skills</text>
  </svg>
  <footer class="footer"><span class="brand">BILDMARK / TERRAMIX</span><span class="date">2/7/2020</span><span class="seal">BILDMARK</span><span class="page">3</span></footer>
</section>

<!-- 4 what to mentor -->
<section class="slide" style="left:22px;top:430px">
  <div class="title" style="top:20px">WHAT TO MENTOR?</div>
  <div class="side-note" style="left:32px;top:195px"><b style="color:var(--red-bright)">How</b> they do their job <b style="color:var(--red-bright)">will</b>.</div>
  <div class="side-note" style="left:542px;top:188px;width:165px">Employees just doing their job will not get them a pay raise or a promotion.</div>
  <svg class="abs" style="left:0;top:0" width="715" height="380" viewBox="0 0 715 380">
    <g transform="translate(358 205)" stroke="#fff" stroke-width="2">
      <path d="M0,-150 A150,150 0 0 1 96.4,-114.9 L41.1,-49 A64,64 0 0 0 0,-64 Z" fill="#4d5fd0"/>
      <path d="M0,-150 A150,150 0 0 1 96.4,-114.9 L41.1,-49 A64,64 0 0 0 0,-64 Z" transform="rotate(40)" fill="#5ac8f0"/>
      <path d="M0,-150 A150,150 0 0 1 96.4,-114.9 L41.1,-49 A64,64 0 0 0 0,-64 Z" transform="rotate(80)" fill="#a6e04a"/>
      <path d="M0,-150 A150,150 0 0 1 96.4,-114.9 L41.1,-49 A64,64 0 0 0 0,-64 Z" transform="rotate(120)" fill="#5cd2b0"/>
      <path d="M0,-150 A150,150 0 0 1 96.4,-114.9 L41.1,-49 A64,64 0 0 0 0,-64 Z" transform="rotate(160)" fill="#fb7d1e"/>
      <path d="M0,-150 A150,150 0 0 1 96.4,-114.9 L41.1,-49 A64,64 0 0 0 0,-64 Z" transform="rotate(200)" fill="#ef4428"/>
      <path d="M0,-150 A150,150 0 0 1 96.4,-114.9 L41.1,-49 A64,64 0 0 0 0,-64 Z" transform="rotate(240)" fill="#2c3a8c"/>
      <path d="M0,-150 A150,150 0 0 1 96.4,-114.9 L41.1,-49 A64,64 0 0 0 0,-64 Z" transform="rotate(280)" fill="#1690c8"/>
      <path d="M0,-150 A150,150 0 0 1 96.4,-114.9 L41.1,-49 A64,64 0 0 0 0,-64 Z" transform="rotate(320)" fill="#6ab02a"/>
      <circle r="64" fill="#3a3a3a" stroke="#fff" stroke-width="3"/>
    </g>
    <g font-family="Arimo,sans-serif" font-size="9" fill="#fff" text-anchor="middle">
      <text x="395" y="104">Teamwork</text>
      <text x="452" y="152">Collaboration</text>
      <text x="466" y="225">Driver</text>
      <text x="428" y="292">No Rumors</text>
      <text x="360" y="318">Low Stress</text>
      <text x="282" y="300">Appreciative</text>
      <text x="255" y="225">Thinking Ahead</text>
      <text x="264" y="162">Actively Engaged</text>
      <text x="321" y="103">No Whining</text>
    </g>
    <rect x="348" y="180" width="20" height="20" rx="2" fill="none" stroke="#fff" stroke-width="1.5"/>
    <line x1="352" y1="186" x2="364" y2="186" stroke="#fff"/><line x1="352" y1="190" x2="364" y2="190" stroke="#fff"/><line x1="352" y1="194" x2="364" y2="194" stroke="#fff"/>
    <text x="358" y="229" text-anchor="middle" font-family="Arimo,sans-serif" font-weight="700" font-size="12" fill="#fff">YOU DOING</text>
    <text x="358" y="244" text-anchor="middle" font-family="Arimo,sans-serif" font-weight="700" font-size="12" fill="#fff">YOUR JOB</text>
  </svg>
  <footer class="footer"><span class="brand">BILDMARK / TERRAMIX</span><span class="date">2/7/2020</span><span class="seal">BILDMARK</span><span class="page">4</span></footer>
</section>

<!-- 5 four disciplines -->
<section class="slide" style="left:748px;top:430px">
  <div class="title">BECOMING A CONSTRUCTION LEADER</div>
  <div class="abs center" style="left:0;right:0;top:53px;font-size:13px">The <span style="color:var(--red-bright)">Four</span> Disciplines</div>
  <div class="panel"></div>
  <svg class="abs" style="left:144px;top:126px" width="48" height="38" viewBox="0 0 48 38"><polygon points="2,18 46,2 30,36 22,24" fill="#5acfb0"/><polygon points="22,24 46,2 26,34" fill="#2eaa87"/></svg>
  <div class="disc" style="left:-2px;top:180px">INCREASING YOUR CAPACITY</div>
  <svg class="abs" style="left:516px;top:122px" width="50" height="40" viewBox="0 0 50 40"><circle cx="30" cy="22" r="14" fill="none" stroke="#fb7d1e" stroke-width="3"/><line x1="30" y1="22" x2="30" y2="13" stroke="#fb7d1e" stroke-width="2"/><line x1="30" y1="22" x2="36" y2="26" stroke="#fb7d1e" stroke-width="2"/><rect x="27" y="3" width="6" height="4" fill="#fb7d1e"/><line x1="2" y1="16" x2="13" y2="16" stroke="#fb7d1e" stroke-width="2.5"/><line x1="5" y1="22" x2="13" y2="22" stroke="#fb7d1e" stroke-width="2.5"/><line x1="2" y1="28" x2="13" y2="28" stroke="#fb7d1e" stroke-width="2.5"/></svg>
  <div class="disc" style="left:356px;top:180px">DRIVING THE RIGHT CULTURE</div>
  <svg class="abs" style="left:143px;top:232px" width="50" height="32" viewBox="0 0 50 32"><g fill="#82d21e"><circle cx="10" cy="8" r="4"/><circle cx="25" cy="6" r="5"/><circle cx="40" cy="8" r="4"/><rect x="4" y="14" width="12" height="12" rx="3"/><rect x="18" y="13" width="14" height="13" rx="3"/><rect x="34" y="14" width="12" height="12" rx="3"/><rect x="0" y="26" width="50" height="4"/></g></svg>
  <div class="disc" style="left:-2px;top:290px">YOUR EMPLOYEES’ LEADERSHIP STYLE</div>
  <svg class="abs" style="left:516px;top:226px" width="54" height="42" viewBox="0 0 54 42"><path d="M2,6 L18,4 L34,18 L30,26 L24,24 L18,32 L10,26 L2,22 Z" fill="#3bb0e8"/><path d="M52,4 L38,4 L26,12 L30,16 L38,12 L48,22 L52,18 Z" fill="#1690c8"/></svg>
  <div class="disc" style="left:356px;top:290px">BEING A TRUST DRIVER</div>
  <footer class="footer"><span class="brand">BILDMARK / TERRAMIX</span><span class="date">2/7/2020</span><span class="seal">BILDMARK</span><span class="page">5</span></footer>
</section>

<!-- 6 capacity -->
<section class="slide" style="left:1475px;top:430px">
  <div class="photo" role="img" aria-label="Photo of a businesswoman on the phone checking her wristwatch"></div>
  <div class="disc-head">Discipline:&nbsp; YOUR <span style="color:var(--red-bright)">CAPACITY</span></div>
  <div class="disc-body">If you could increase your <b style="font-weight:700;color:#3cc6a0">capacity</b>, what should you use this additional time to do?</div>
  <footer class="footer"><span class="brand">BILDMARK / TERRAMIX</span><span class="date">2/7/2020</span><span class="seal">BILDMARK</span><span class="page">6</span></footer>
</section>

<!-- 7 six ways -->
<section class="slide" style="left:22px;top:843px">
  <div class="title" style="left:-20px">THE 6 WAYS TO COMMUNICATE</div>
  <table class="comm-grid">
    <tr>
      <td><svg width="34" height="22" viewBox="0 0 34 22"><ellipse cx="17" cy="11" rx="16" ry="9" fill="#9aa6e6"/><circle cx="17" cy="11" r="6" fill="#5a6ad0"/><circle cx="17" cy="11" r="2.5" fill="#fff"/></svg><span>A LOOK</span></td>
      <td><svg width="28" height="26" viewBox="0 0 28 26"><ellipse cx="14" cy="11" rx="13" ry="10" fill="#3bb0e8"/><polygon points="5,17 3,25 12,19" fill="#3bb0e8"/></svg><span>A WORD</span></td>
      <td><svg width="34" height="26" viewBox="0 0 34 26" font-family="Archivo Black,sans-serif"><text x="0" y="32" font-size="44" fill="#82d21e">”</text></svg><span>A SENTENCE</span></td>
    </tr>
    <tr>
      <td><svg width="30" height="30" viewBox="0 0 30 30"><rect x="2" y="4" width="20" height="24" fill="none" stroke="#5acfb0" stroke-width="2"/><line x1="6" y1="11" x2="16" y2="11" stroke="#5acfb0" stroke-width="2"/><line x1="6" y1="17" x2="14" y2="17" stroke="#5acfb0" stroke-width="2"/><line x1="14" y1="24" x2="28" y2="8" stroke="#5acfb0" stroke-width="3"/></svg><span>A PARAGRAPH</span></td>
      <td><svg width="34" height="26" viewBox="0 0 34 26"><path d="M2,3 L16,5 L16,24 L2,22 Z M32,3 L18,5 L18,24 L32,22 Z" fill="none" stroke="#fb7d1e" stroke-width="2"/><line x1="5" y1="10" x2="13" y2="11" stroke="#fb7d1e"/><line x1="5" y1="15" x2="13" y2="16" stroke="#fb7d1e"/><line x1="21" y1="11" x2="29" y2="10" stroke="#fb7d1e"/><line x1="21" y1="16" x2="29" y2="15" stroke="#fb7d1e"/></svg><span>A CHAPTER</span></td>
      <td><svg width="28" height="30" viewBox="0 0 28 30"><path d="M8,2 L26,2 L22,24 L4,24 Z" fill="#e8382a"/><path d="M4,24 L22,24 L21,28 L3,28 Z" fill="#f59a8f"/></svg><span>A BOOK</span></td>
    </tr>
  </table>
  <svg class="abs" style="left:540px;top:75px" width="100" height="265" viewBox="0 0 100 265">
    <polygon points="68,2 96,44 84,44 84,258 52,258 52,44 40,44" fill="#2eaa87"/>
    <polygon points="33,32 61,74 50,74 50,258 20,258 20,74 6,74" fill="#17a8e6"/>
    <text transform="translate(40 200) rotate(-90)" font-family="Archivo,sans-serif" font-size="13" letter-spacing="3" fill="#fff">VELOCITY</text>
    <text transform="translate(73 185) rotate(-90)" font-family="Archivo,sans-serif" font-size="13" letter-spacing="3" fill="#fff">CAPACITY</text>
  </svg>
  <footer class="footer"><span class="brand">BILDMARK / TERRAMIX</span><span class="date">2/7/2020</span><span class="seal">BILDMARK</span><span class="page">7</span></footer>
</section>

<!-- 8 research -->
<section class="slide" style="left:748px;top:843px">
  <div class="title" style="top:22px">RESEARCH</div>
  <div class="stat" style="left:21px;background:var(--teal)"><div class="num">25<sup>%</sup></div><div class="lbl" style="background:var(--teal-dark)">ACTIVELY ENGAGED</div></div>
  <div class="stat" style="left:246px;background:var(--orange)"><div class="num">50<sup>%</sup></div><div class="lbl" style="background:var(--orange-dark)">RIDING ALONG</div></div>
  <div class="stat" style="left:471px;background:var(--red-bright)"><div class="num">25<sup>%</sup></div><div class="lbl" style="background:#c82a1e">ACTIVELY DISENGAGED</div></div>
  <footer class="footer"><span class="brand">BILDMARK / TERRAMIX</span><span class="date">2/7/2020</span><span class="seal">BILDMARK</span><span class="page">8</span></footer>
</section>

<!-- 9 quadrant -->
<section class="slide" style="left:1475px;top:843px">
  <div class="axis-lbl" style="left:312px;top:40px">HIGH EFFORT</div>
  <div class="axis-lbl" style="left:312px;top:344px">LOW EFFORT</div>
  <div class="vert axis-lbl" style="left:62px;top:270px">LOW AGREEMENT</div>
  <div class="vert axis-lbl" style="left:636px;top:272px">HIGH AGREEMENT</div>
  <svg class="abs" style="left:0;top:0" width="715" height="380" viewBox="0 0 715 380">
    <polygon points="357,78 376,112 365,112 365,296 376,296 357,326 338,296 349,296 349,112 338,112" fill="#c6ece1"/>
    <polygon points="102,202 135,184 135,196 580,196 580,184 613,202 580,220 580,208 135,208 135,220" fill="#c6ece1"/>
  </svg>
  <div class="quad" style="left:137px;top:114px;background:var(--red-bright)"><b>CONCESSION</b><i>Riding Along</i></div>
  <div class="quad" style="left:365px;top:114px;background:var(--orange)"><b>BUY-IN</b><i>Highly Engaged</i></div>
  <div class="quad" style="left:137px;top:210px;background:var(--green)"><b>RESENTMENT</b><i>Highly Disengaged</i></div>
  <div class="quad" style="left:365px;top:210px;background:var(--teal)"><b>EXEMPT</b><i>Riding Along</i></div>
  <footer class="footer"><span class="brand">BILDMARK / TERRAMIX</span><span class="date">2/7/2020</span><span class="seal">BILDMARK</span><span class="page">9</span></footer>
</section>

<!-- 10 engagement table -->
<section class="slide" style="left:22px;top:1257px">
  <div class="eng-head">HOW CAN YOU HELP FELLOW EMPLOYEES BE HIGHLY ENGAGED?</div>
  <div class="figure" role="img" aria-label="Silhouette illustration of an engaged businessman" style="left:58px;top:36px;width:80px;height:318px;border-radius:30px 30px 4px 4px"></div>
  <div class="figure" role="img" aria-label="Silhouette illustration of a disengaged businessman" style="left:565px;top:44px;width:78px;height:310px;border-radius:30px 30px 4px 4px;background:linear-gradient(180deg,#23284a,#151832)"></div>
  <div class="vert" style="left:24px;top:246px;color:var(--teal)">HIGHLY ENGAGED</div>
  <div class="vert" style="left:680px;top:252px;color:var(--orange)">LOW / NO ENGAGED</div>
  <div class="abs" style="left:136px;top:42px;font-size:9.5px;line-height:12px">Proportion of highly engaged employees<br>experiencing this</div>
  <div class="abs" style="left:385px;top:44px;font-size:9.5px;line-height:12px;text-align:right;width:196px">Proportion of low / no engaged employees<br>experiencing this</div>
  <svg class="abs" style="left:120px;top:66px" width="470" height="8"><line x1="4" y1="4" x2="464" y2="4" stroke="#f4b84a" stroke-dasharray="2 2"/><circle cx="4" cy="4" r="3" fill="#f4a42a"/><circle cx="464" cy="4" r="3" fill="#f4a42a"/></svg>
  <table class="eng-table">
    <tr><td class="hi">92%</td><td>Someone has talked about their progress</td><td class="lo">13%</td></tr>
    <tr><td class="hi">97%</td><td>Someone encourages their development</td><td class="lo">10%</td></tr>
    <tr><td class="hi">88%</td><td>They have been praised recently</td><td class="lo">13%</td></tr>
    <tr><td class="hi">98%</td><td>They have opportunities to learn and grow</td><td class="lo">13%</td></tr>
    <tr><td class="hi">74%</td><td>They have a best friend at work</td><td class="lo">19%</td></tr>
    <tr><td class="hi">98%</td><td>Their manager cares about them</td><td class="lo">20%</td></tr>
    <tr><td class="hi">98%</td><td>They view their job as important to the company</td><td class="lo">22%</td></tr>
    <tr><td class="hi">91%</td><td>Their opinions count at work</td><td class="lo">19%</td></tr>
    <tr><td class="hi">93%</td><td>Their colleagues are committed to quality work</td><td class="lo">44%</td></tr>
    <tr><td class="hi">99%</td><td>They are able to do their best every day</td><td class="lo">53%</td></tr>
    <tr class="flag"><td class="hi">98%</td><td>They have equipment needed to do their job</td><td class="lo">70%</td></tr>
    <tr class="flag"><td class="hi">99%</td><td>They know what is expected of them at work</td><td class="lo">89%</td></tr>
  </table>
  <footer class="footer"><span class="brand">BILDMARK / TERRAMIX</span><span class="date">2/7/2020</span><span class="seal">BILDMARK</span><span class="page">10</span></footer>
</section>

<!-- 11 fatigue -->
<section class="slide" style="left:748px;top:1257px">
  <div class="fat-head">Employees that CREATE FATIGUE, have a HIGH EFQ, and have<br>the following attributes:</div>
  <ul class="fat-list" style="left:55px">
    <li>Inability to make decisions</li><li>Lack of confidence</li><li>Negative</li><li>An abundance of venting their feelings</li><li>Lack of maturity and professionalism</li><li>More of a passenger mindset versus driver mindset</li><li>Need input on small stuff</li><li>High Maintenance</li><li>Constantly need high praise for normal stuff</li><li>Low Initiative</li><li>Never offer solutions</li><li>Underlying negativity</li><li>Complain a lot</li>
  </ul>
  <ul class="fat-list" style="left:364px">
    <li>Actively work to do the bare minimum</li><li>Hard time prioritizing</li><li>Require hovering</li><li>More mistakes</li><li>Over think things</li><li>Don’t meet deadlines</li><li>Not punctual</li><li>High drama</li><li>Bad body language</li><li>Highly stressed</li><li>Push back on everything</li><li>Don’t trust other’s work</li><li>Entitlement attitude</li>
  </ul>
  <footer class="footer"><span class="brand">BILDMARK / TERRAMIX</span><span class="date">2/7/2020</span><span class="seal">BILDMARK</span><span class="page">11</span></footer>
</section>

<!-- 12 thank you -->
<section class="slide" style="left:1475px;top:1257px">
  <div class="brandmark" style="top:60px"><span class="dot" style="width:72px;height:72px"></span>BILDMARK/TERRAMIX</div>
  <div class="thanks">THANK YOU</div>
  <div class="abs center" style="left:0;right:0;top:245px;font-size:17px">Your subtitle here</div>
  <div class="contact" style="left:0;background:var(--green)"><svg width="20" height="20" viewBox="0 0 20 20" fill="none" stroke="#fff" stroke-width="1.3"><circle cx="10" cy="10" r="8.5"/><ellipse cx="10" cy="10" rx="4" ry="8.5"/><line x1="1.5" y1="10" x2="18.5" y2="10"/></svg>https://bildmarkterramix.com/</div>
  <div class="contact" style="left:179px;background:var(--teal-dark)"><svg width="22" height="20" viewBox="0 0 22 20" fill="none" stroke="#fff" stroke-width="1.3"><rect x="1" y="3" width="20" height="14"/><polyline points="1,3 11,11 21,3"/></svg>events@showplanner-co.com</div>
  <div class="contact" style="left:358px;background:var(--orange-dark)"><svg width="20" height="20" viewBox="0 0 20 20" fill="none" stroke="#fff" stroke-width="1.3"><path d="M4,2 L8,6 L6,9 Q9,13 11,14 L14,12 L18,16 L15,19 Q6,16 1,5 Z"/></svg>+1-555-014-2290</div>
  <div class="contact" style="left:537px;background:#c8280e;width:178px"><svg width="18" height="20" viewBox="0 0 18 20" fill="none" stroke="#fff" stroke-width="1.3"><path d="M9,19 Q2,11 2,7 A7,7 0 0 1 16,7 Q16,11 9,19 Z"/><circle cx="9" cy="7" r="2.5"/></svg>Sandridge, NV</div>
</section>

</div>
</body>
</html>
```